Real Estate Business Cards

Looking for a clean, sharp and professional look for our Real Estate investment Fund that invests in Multi Family Apartment buildings.

Target Market(s)

Real Estate Fund

Industry/Entity Type

Real Estate

Contact Information for Business Card

Company Description: Real Estate Investment Fund
Company Name: RKW Holdings
Name: Marcus Olvane
Cell: (917) 482-0657
Email: marcus@rkwholdings-example.com
Website: www.rkwholdings-example.com
Address: 418, 9th Street, Brooklyn NY 11218

Colors

Designer to choose colors to be used in the design.

Requirements
Nice to have
• Colors to match logo

```html
<!DOCTYPE html>
<html lang="en">
<head>
<meta charset="utf-8">
<title>RKW Holdings – Business Cards</title>
<link href="https://fonts.googleapis.com/css2?family=Lato:wght@400;700;900&display=swap" rel="stylesheet">
<style>
  :root{
    --blue:#0f6fab;
    --blue-dark:#0b5a8c;
    --grey:#4a4a4c;
    --white:#ffffff;
    --bg:#e9ecef;
    --card-w:600px;
    --card-h:343px;
  }
  *{box-sizing:border-box;margin:0;padding:0}
  html,body{width:1200px;height:835px;overflow:hidden}
  body{
    background:var(--bg);
    font-family:"Lato",Arial,sans-serif;
    position:relative;
  }
  .card{
    position:absolute;
    width:var(--card-w);
    height:var(--card-h);
    border-radius:22px;
    overflow:hidden;
    box-shadow:0 8px 22px rgba(0,0,0,.18);
  }
  .card--front{left:90px;top:50px;background:var(--white)}
  .card--back{left:510px;top:442px;background:var(--blue)}

  .front-shape{position:absolute;inset:0;width:100%;height:100%}

  .wordmark{
    position:absolute;
    display:flex;align-items:center;gap:10px;
    font-weight:700;font-size:30px;letter-spacing:.5px;
  }
  .wordmark__mark{width:26px;height:26px;display:block}
  .card--front .wordmark{right:38px;top:56px;color:var(--blue)}
  .card--front .wordmark__mark{background:var(--blue)}
  .card--back .wordmark{left:44px;top:60px;color:var(--white)}
  .card--back .wordmark__mark{background:var(--white)}

  .holder{
    position:absolute;left:58px;top:222px;color:var(--white);
  }
  .holder__name{font-weight:700;font-size:22px;line-height:28px;margin-bottom:10px}
  .contact{list-style:none;font-size:15px;line-height:22px}
  .contact li{display:flex;align-items:center;gap:9px}
  .contact svg{width:15px;height:15px;flex:none}

  .tagline{
    position:absolute;right:0;top:150px;
    width:300px;height:44px;
    background:var(--white);color:var(--blue);
    font-weight:900;font-size:21px;
    display:flex;align-items:center;justify-content:center;
  }
  .address{
    position:absolute;left:250px;right:20px;top:250px;
    color:var(--white);text-align:center;
  }
  .address__company{font-weight:700;font-size:17px;margin-bottom:4px}
  .address__street{font-size:16px}
</style>
</head>
<body>

<section class="card card--front" aria-label="Business card front">
  <svg class="front-shape" viewBox="0 0 600 343" preserveAspectRatio="none" aria-hidden="true">
    <polygon points="0,230 115,152 600,182 600,190 118,162 0,243" fill="var(--grey)"/>
    <polygon points="0,250 120,170 600,198 600,343 0,343" fill="var(--blue)"/>
  </svg>
  <div class="wordmark"><span class="wordmark__mark"></span>RKW Holdings</div>
  <div class="holder">
    <p class="holder__name">Marcus Olvane</p>
    <ul class="contact">
      <li><svg viewBox="0 0 16 16"><rect x="4" y="1" width="8" height="14" rx="1.5" fill="none" stroke="#fff" stroke-width="1.5"/><circle cx="8" cy="12.5" r="0.9" fill="#fff"/></svg>(917) 482-0657</li>
      <li><svg viewBox="0 0 16 16"><rect x="1" y="3" width="14" height="10" fill="none" stroke="#fff" stroke-width="1.5"/><path d="M1 3 L8 9 L15 3" fill="none" stroke="#fff" stroke-width="1.5"/></svg>marcus@rkwholdings-example.com</li>
      <li><svg viewBox="0 0 16 16"><rect x="1" y="2" width="14" height="10" rx="1" fill="none" stroke="#fff" stroke-width="1.5"/><path d="M5 15 H11 M8 12 V15" stroke="#fff" stroke-width="1.5"/></svg>www.rkwholdings-example.com</li>
    </ul>
  </div>
</section>

<section class="card card--back" aria-label="Business card back">
  <div class="wordmark"><span class="wordmark__mark"></span>RKW Holdings</div>
  <div class="tagline">Real Estate Investment Fund</div>
  <div class="address">
    <p class="address__company">RKW Holdings</p>
    <p class="address__street">418, 9th Street, Brooklyn NY 11218</p>
  </div>
</section>

</body>
</html>
```